Business Card Design

Business card design.

Business card is to have logo, website address and email address.

Website is www.brightkettle.ie
Email is info@brightkettle.ie
Logo uploaded

I have ordered Business Card Printing via Print Harbor, the Double-sided colour printed option with gloss finish.

Industry/Entity Type

Business

```html
<!DOCTYPE html>
<html lang="en">
<head>
<meta charset="utf-8">
<title>Bright Kettle business cards</title>
<link rel="stylesheet" href="https://fonts.googleapis.com/css2?family=Montserrat:wght@400;600;800&display=swap">
<style>
  :root {
    --stage: #d8d2cb;
    --card: #ffffff;
    --red: #d81f26;
    --red-deep: #a8141c;
    --ink: #1c1c1c;
    --grey: #9a9ca0;
    --label: #2b2b2b;
  }
  * { margin: 0; padding: 0; box-sizing: border-box; }
  html, body { width: 1200px; height: 800px; overflow: hidden; }
  body {
    background: var(--stage);
    font-family: "Montserrat", sans-serif;
    position: relative;
  }
  .card-label {
    position: absolute;
    width: 509px;
    text-align: center;
    font-size: 22px;
    font-weight: 400;
    color: var(--label);
  }
  .card {
    position: absolute;
    width: 509px;
    height: 290px;
    border-radius: 18px;
    background: var(--card);
    box-shadow: 0 6px 16px rgba(0,0,0,0.25);
    overflow: hidden;
  }
  .card--red { background: linear-gradient(180deg, var(--red) 0%, var(--red-deep) 100%); }

  .pos-front { left: 72px; top: 91px; }
  .pos-back1 { left: 621px; top: 91px; }
  .pos-back2 { left: 72px; top: 450px; }
  .pos-back3 { left: 621px; top: 450px; }
  .label-front { left: 72px; top: 48px; }
  .label-back1 { left: 621px; top: 48px; }
  .label-back2 { left: 72px; top: 406px; }
  .label-back3 { left: 621px; top: 406px; }

  .brand {
    position: absolute;
    left: 0; right: 0;
    display: flex;
    flex-direction: column;
    align-items: center;
    gap: 10px;
  }
  .brand-dot {
    border-radius: 50%;
    background: var(--red);
  }
  .brand-name {
    font-weight: 800;
    color: var(--ink);
    letter-spacing: -0.5px;
  }
  .card--red .brand-dot { background: #ffffff; }
  .card--red .brand-name { color: #ffffff; }

  .front-brand { top: 48px; }
  .front-brand .brand-dot { width: 50px; height: 50px; }
  .front-brand .brand-name { font-size: 34px; }

  .back-brand { top: 82px; }
  .back-brand .brand-dot { width: 58px; height: 58px; }
  .back-brand .brand-name { font-size: 40px; }

  .back-brand--large { top: 70px; }
  .back-brand--large .brand-dot { width: 116px; height: 116px; }

  .web-line {
    position: absolute;
    left: 0; right: 0;
    bottom: 26px;
    text-align: center;
    font-size: 15px;
    letter-spacing: 4px;
    color: var(--ink);
  }
  .card--red .web-line { color: #ffffff; }

  .swoosh { position: absolute; left: 0; top: 0; }
  .contact {
    position: absolute;
    left: 30px;
    bottom: 14px;
    color: #ffffff;
    font-size: 14px;
    line-height: 19px;
  }
  .contact b { font-weight: 800; font-style: italic; }
</style>
</head>
<body>
  <div class="card-label label-front">Front</div>
  <div class="card-label label-back1">Back - 1</div>
  <div class="card-label label-back2">Back - 2</div>
  <div class="card-label label-back3">Back - 3</div>

  <section class="card pos-front">
    <div class="brand front-brand">
      <span class="brand-dot"></span>
      <span class="brand-name">BRIGHTKETTLE.IE</span>
    </div>
    <svg class="swoosh" width="509" height="290" viewBox="0 0 509 290">
      <path d="M0,203 C160,212 360,262 509,236 L509,290 L0,290 Z" fill="var(--red)"/>
      <path d="M40,208 C200,230 380,280 509,246" fill="none" stroke="var(--grey)" stroke-width="7"/>
      <path d="M150,214 C300,248 430,262 509,222" fill="none" stroke="var(--ink)" stroke-width="8"/>
    </svg>
    <div class="contact">
      <div><b>email</b> : info@brightkettle.ie</div>
      <div><b>web</b> : www.brightkettle.ie</div>
    </div>
  </section>

  <section class="card pos-back1">
    <div class="brand back-brand">
      <span class="brand-dot"></span>
      <span class="brand-name">BRIGHTKETTLE.IE</span>
    </div>
    <div class="web-line">www.brightkettle.ie</div>
  </section>

  <section class="card pos-back2">
    <div class="brand back-brand--large">
      <span class="brand-dot"></span>
    </div>
    <div class="web-line">www.brightkettle.ie</div>
  </section>

  <section class="card card--red pos-back3">
    <div class="brand back-brand">
      <span class="brand-dot"></span>
      <span class="brand-name">BRIGHTKETTLE.IE</span>
    </div>
    <div class="web-line">www.brightkettle.ie</div>
  </section>
</body>
</html>
```